Dorsey K. Wendell Business Card

We need a business card for our company Dorsey K. Wendell Heating & Plumbing to be distributed to potential customers. It should follow the color scheme of our logo and have a modern upscale and masculine look.

The logo is attached and the info below should also be included:

5187 W. Cedar Brook Rd.
Fernbrook, PA 17630

Russell T. Wendell
(717) 592-0817
russelltwendell@fernmail.net
dorseykwendell.net
PA #093148

Industry/Entity Type

Business

Contact Information for Business Card

5187 W. Cedar Brook Rd.
Fernbrook, PA 17630

Russell T. Wendell
(717) 592-0817
russelltwendell@fernmail.net
dorseykwendell.net
PA #093148

Colors

Designer to choose colors to be used in the design.

Requirements
Must have
• Information above included

```html
<!DOCTYPE html>
<html lang="en">
<head>
<meta charset="utf-8">
<title>Dorsey K. Wendell Business Card</title>
<link href="https://fonts.googleapis.com/css2?family=Roboto:wght@400;700&family=Roboto+Condensed:wght@700&display=swap" rel="stylesheet">
<style>
  :root {
    --backdrop: #2a2a2a;
    --paper: #f4f4f2;
    --brand-blue: #0a57a4;
    --ink-grey: #5a5a5a;
    --white: #ffffff;
  }
  * { box-sizing: border-box; margin: 0; padding: 0; }
  html, body { width: 1200px; height: 960px; overflow: hidden; }
  body {
    background: var(--backdrop);
    position: relative;
    font-family: "Roboto", Arial, sans-serif;
  }
  .card {
    position: absolute;
    left: 320px;
    width: 600px;
    height: 342px;
    overflow: hidden;
  }
  .card-front { top: 103px; background: var(--paper); }
  .card-back { top: 493px; background: var(--brand-blue); color: var(--white); }

  .brand-name {
    display: flex;
    align-items: center;
    gap: 10px;
    font-family: "Roboto Condensed", "Arial Narrow", sans-serif;
    font-weight: 700;
    text-transform: uppercase;
    line-height: 1.05;
  }
  .brand-mark { flex: none; }
  .card-front .brand-name {
    position: absolute;
    left: 0; right: 0;
    top: 132px;
    justify-content: center;
    color: var(--brand-blue);
    font-size: 30px;
  }
  .card-front .brand-mark { width: 58px; height: 58px; background: var(--brand-blue); }
  .brand-sub { display: block; font-size: 0.55em; letter-spacing: 0.08em; }

  .front-web {
    position: absolute;
    left: 0; right: 0;
    top: 298px;
    text-align: center;
    font-size: 14px;
    letter-spacing: 0.42em;
    color: var(--ink-grey);
  }

  .back-block {
    position: absolute;
    left: 38px;
    top: 28px;
    width: 224px;
    height: 226px;
    background: var(--paper);
  }
  .card-back .brand-name {
    position: absolute;
    right: 32px;
    top: 34px;
    color: var(--white);
    font-size: 24px;
  }
  .card-back .brand-mark { width: 42px; height: 42px; background: var(--white); }

  .contact {
    position: absolute;
    right: 32px;
    top: 150px;
    text-align: right;
    font-size: 15px;
    line-height: 20px;
  }
  .contact-name {
    font-family: "Roboto Condensed", "Arial Narrow", sans-serif;
    font-weight: 700;
    font-size: 21px;
    margin-bottom: 12px;
  }
  .contact-address { margin-bottom: 8px; }
  .contact-line { display: flex; justify-content: flex-end; align-items: center; gap: 8px; }
  .contact-line svg { width: 13px; height: 13px; fill: var(--white); }
</style>
</head>
<body>

<section class="card card-front">
  <div class="brand-name">
    <span class="brand-mark"></span>
    <span>Dorsey K. Wendell<span class="brand-sub">Heating &amp; Plumbing</span></span>
  </div>
  <p class="front-web">www.dorseykwendell.net</p>
</section>

<section class="card card-back">
  <div class="back-block"></div>
  <div class="brand-name">
    <span class="brand-mark"></span>
    <span>Dorsey K. Wendell<span class="brand-sub">Heating &amp; Plumbing</span></span>
  </div>
  <div class="contact">
    <p class="contact-name">RUSSELL T. WENDELL</p>
    <p class="contact-address">5187 W. Cedar Brook Rd.<br>Fernbrook, PA 17630</p>
    <p class="contact-line">(717) 592-0817
      <svg viewBox="0 0 24 24"><path d="M6.6 10.8a15 15 0 0 0 6.6 6.6l2.2-2.2a1 1 0 0 1 1-.25 11.4 11.4 0 0 0 3.6.57 1 1 0 0 1 1 1V20a1 1 0 0 1-1 1A17 17 0 0 1 3 4a1 1 0 0 1 1-1h3.5a1 1 0 0 1 1 1c0 1.25.2 2.45.57 3.57a1 1 0 0 1-.25 1z"/></svg>
    </p>
    <p class="contact-line">russelltwendell@fernmail.net
      <svg viewBox="0 0 24 24"><path d="M2 6.5V19h20V6.5l-10 7.5z M2.8 5h18.4L12 11.9z"/></svg>
    </p>
    <p class="contact-line">dorseykwendell.net
      <svg viewBox="0 0 24 24"><circle cx="12" cy="12" r="10"/><path d="M2 12h20M12 2c3 3 3 17 0 20M12 2c-3 3-3 17 0 20" stroke="#0a57a4" stroke-width="1.6" fill="none"/></svg>
    </p>
    <p class="contact-line">PA #093148</p>
  </div>
</section>

</body>
</html>
```